Visualisation Software brochure

i need a sales brochure for a new visualisation software company called Lumora Scene Studio.
The software has been specifically designed for manufacturers, distributers and retailers in the design / décor / furnishing / building industries. It allows customers can then import unlimited numbers of digital photos of rooms from their own home or take advantage of a library of pre-made photos, and then render different products from your catalogue into that photo to see what the finished look will be.
i have attached:
1) a mock up of the home page of the website
2) example of brochure wording that i have put together (although i am a little unsure about what other words i can add - so any suggestions here would be good)
3) i have attached some examples of other brochures that i like and would like similar designs
I am after a classy brochure used by a large corporate technology company that is given to executives and gives an impression of quality, trustworthiness and innovation.
• the colour blue as per the colours on my website mock up provided in the design brief
• I like simple, smart, clean and uncluttered design
• I like simple, clean and uncluttered design
• I like pictures that fit in with my technology (whether that be home and interior design, mixing virtual world and real world, visualising an idea) rather than basic stock of corporate people
Updates
Target Market(s)
marketing professionals
Industry/Entity Type
Software
Font styles to use
Look and feel
Each slider illustrates characteristics of the customer's brand and the style your logo design should communicate.

```html
<!DOCTYPE html>
<html lang="en">
<head>
<meta charset="utf-8">
<title>Lumora Scene Studio – Brochure</title>
<link href="https://fonts.googleapis.com/css2?family=PT+Sans:wght@400;700&display=swap" rel="stylesheet">
<style>
:root{
  --blue:#2b5b9c;
  --logo-blue:#2e5fa8;
  --text:#3a3a3a;
  --panel:#e6e6ea;
  --panel-line:#c9c9cf;
  --white:#ffffff;
  --rule:#6f6f75;
}
*{box-sizing:border-box;margin:0;padding:0}
html,body{width:1200px;height:849px;overflow:hidden;background:var(--white)}
body{font-family:"PT Sans",Arial,sans-serif;color:var(--text)}
.brochure{position:relative;width:1200px;height:849px;overflow:hidden;background:var(--white)}
.block{position:absolute}
.photo{position:absolute}
.photo--analyst{left:0;top:0;width:259px;height:322px;background:linear-gradient(135deg,#dfe9f3 0%,#9fb8d3 55%,#cfd9e4 100%)}
.photo--hologram{left:279px;top:322px;width:357px;height:226px;background:radial-gradient(ellipse at 50% 55%,#d9e2ec 0%,#7f93ab 45%,#2b3a52 100%)}
.photo--team{left:599px;top:0;width:601px;height:357px;background:linear-gradient(120deg,#2c4f86 0%,#7da3cf 45%,#dce6ef 75%,#39557f 100%)}
.photo--celebrate{left:985px;top:552px;width:215px;height:292px;background:linear-gradient(180deg,#ffffff 0%,#eceef1 50%,#c9ccd2 100%)}
.panel--challenge{left:0;top:322px;width:259px;height:486px;background:var(--panel)}
.panel--retail{left:636px;top:357px;width:564px;height:191px;background:var(--panel)}
.panel--retail-tab{left:636px;top:322px;width:274px;height:36px;background:var(--panel)}
.panel--consumer{left:599px;top:548px;width:601px;height:301px;border:1px solid var(--panel-line);border-right:none;border-bottom:none}
.divider-mid{position:absolute;left:259px;top:808px;width:1px;height:41px;background:var(--panel-line)}
.brand{position:absolute;left:279px;top:26px;display:flex;align-items:center;gap:9px}
.brand__dot{width:30px;height:30px;border-radius:50%;background:var(--logo-blue)}
.brand__name{font-size:11.5px;font-weight:400;color:#2a2a2a}
.brand-rule{position:absolute;left:443px;top:42px;width:292px;height:2px;background:var(--rule)}
.section-title{position:absolute;left:646px;top:12px;font-size:24px;font-weight:400;color:var(--white)}
h2{font-weight:400;color:var(--blue);font-size:19px;line-height:21px}
p{font-size:9.6px;line-height:14.1px;text-align:justify;margin-bottom:6px}
.col-challenge{left:28px;top:336px;width:217px}
.col-challenge h2{margin-bottom:10px}
.col-solution{left:279px;top:86px;width:280px}
.col-solution h2{margin-bottom:8px}
.col-solution-cont{left:279px;top:552px;width:280px}
.col-solution-cont p{margin-bottom:5px}
ul{list-style:none}
li{position:relative;padding-left:8px;font-size:9.6px;line-height:14.1px;margin-bottom:5px}
li::before{content:"•";position:absolute;left:0;top:0;color:var(--blue)}
.col-retail{left:664px;top:336px;width:506px}
.col-retail h2{margin-bottom:7px}
.col-consumer{left:664px;top:566px;width:234px}
.col-consumer h2{margin-bottom:8px}
.col-consumer li{text-align:justify;margin-bottom:6px}
</style>
</head>
<body>
<main class="brochure">

  <div class="photo photo--analyst" role="img" aria-label="Businessman studying a tablet in front of a digital world map"></div>
  <div class="block panel--challenge"></div>
  <div class="photo photo--team" role="img" aria-label="Business team around a table with tablets and glowing network connections"></div>
  <div class="block panel--retail-tab"></div>
  <div class="block panel--retail"></div>
  <div class="block panel--consumer"></div>
  <div class="photo photo--hologram" role="img" aria-label="Man framing floating holographic screens showing interior room designs"></div>
  <div class="photo photo--celebrate" role="img" aria-label="Cheerful businesswoman raising her arms in front of blurred colleagues"></div>
  <div class="divider-mid"></div>

  <div class="brand">
    <span class="brand__dot"></span>
    <span class="brand__name">Lumora Scene Studio</span>
  </div>
  <div class="brand-rule"></div>
  <div class="section-title">Benefits</div>

  <section class="block col-challenge">
    <h2>The challenge for both customers and retailers</h2>
    <p>Gone are the days when all you needed was a showroom, a product line, and a business card. Customers are better informed, more interactive, and more selective than ever before. With access to a range of new technologies and a wide variety of online resources, these connected consumers are increasingly demanding a dynamic, seamless, integrated, consistent, accessible and personalised experience with your brand across all online, bricks-and-mortar and mobile channels.</p>
    <p>The customer must be empowered to interact across all touchpoints and channels; they want to browse and buy on their own schedules and retailers must offer equally accurate and immediate access to products and customer service. Consumers want to be inspired and be given the tools, advice and confidence to create unique, personal spaces - meaning companies need to feed this design dream and appealing to their vision is essential. The shopping experience should be built around the new reality that most consumers make their browsing and purchasing commitments online, often before they ever see the product in person.</p>
    <p>Amid ongoing economic uncertainty, true omni-channel retailers need to continue to focus on understanding the customer psyche and leveraging innovation to drive loyalty and customer engagement and ultimately increase sales.</p>
  </section>

  <section class="block col-solution">
    <h2>The virtualised solution</h2>
    <p>Having your own branded virtual design software embedded on your website or accessible via an Droidix and/or Pomelo app will help bridge the gap between your customers' design dreams and your products. Our software helps solve one of the biggest problems many experience whilst redecorating or designing their home, which is despite looking at numerous samples, most cannot visualise or conceptualise what the finished look will be.</p>
    <p>It doesn't matter what business you're in. Your customers will be able to visualise all possible product combinations for their new home – it just depends on your range. The software can easily handle 'flat surface products' including roofing, cladding, garage doors, windows and driveways/pathways to interior products such as carpet, tiles, timber and laminate flooring, doors, art works, bench tops and splashbacks.</p>
  </section>

  <section class="block col-solution-cont">
    <p>Importantly, our technology can also handle any product in 3D - whether it be furniture, lighting, floor rugs, curtains / blinds, wardrobes, household items, kitchen cabinets and bathroom fixtures. A truly unique feature allows customers to simply delete the existing item from their photo and replace it with another product from your catalogue without removing any item physically.</p>
    <p>Today's consumer doesn't just rely on technological gimmicks such as augmented reality or one in-store visit before making important investment decisions. With so much competition in the marketplace consumers are more driven than ever to shop around with the amount and quality of value-adding service the real deal breaker rather than price.</p>
    <p>It has become more about initiating the education of your customer versus waiting for them to ask for assistance. Using our technology can increase sales conversion rates as once customers have identified what products they would like to purchase they come to you as educated buyers, already having experienced a fantastic customer interaction with your brand.</p>
  </section>

  <section class="block col-retail">
    <h2>Retailer Benefits:</h2>
    <ul>
      <li>Be the market innovator and leader by combining technology and a dynamic, seamless, integrated and consistent level of customer service across all online, bricks-and-mortar and mobile channels that delivers the big wow factor</li>
      <li>Extend your reach - don't limit your technology footprint by only using Pomelo apps - our solution leverages and optimises all mobile devices and desktops (PomeloOS, Droidix, Web). This equates to a larger watershed of customers and more sales</li>
      <li>Increase brand engagement as our bespoke and scalable visualisation application will help customers build a relationship with your company, brand, and products and then share that experience within their social circles</li>
      <li>Understand buyer behaviour by receiving real usage statistics to obtain valuable insight about your customers and conduct trend analysis to determine how your future strategies can further enhance your bottom-line</li>
      <li>Increased sales to further grow your business</li>
      <li>Maximise the exposure of your products by uploading your entire product catalogue into a visualisation software that makes them look real</li>
    </ul>
  </section>

  <section class="block col-consumer">
    <h2>Consumer Benefits:</h2>
    <ul>
      <li>Reduce your customer's purchase anxiety as they will have the knowledge that the products they are choosing from your range are the right choice</li>
      <li>Greater flexibility in the way they shop by being open 24/7 and being able to engage with your brand when they want and how they want. Happier customers and hence more sales.</li>
      <li>An easy-to-use interface along with guided help and tutorials for those less confident with technology</li>
      <li>Being able to make informed purchasing decisions as they can easily compare a large range of your products at the touch of a computer key</li>
      <li>Improved personalised buying experience by enabling customers to use photos of their own personal spaces and incorporate your products</li>
    </ul>
  </section>

</main>
</body>
</html>
```